Surveillance Sign

Design sign and stickers with a line drawing of the camera.

Industry/Entity Type

Camera

Requirements
Nice to have
• I like this design: http://www.varnotek.com/cctv-camera-warning-signs-decals/camera-surveillance-sign

```html
<!DOCTYPE html>
<html lang="en">
<head>
<meta charset="utf-8">
<title>Surveillance Sign</title>
<link rel="stylesheet" href="https://fonts.googleapis.com/css2?family=Jost:wght@600;700&display=swap">
<style>
  :root {
    --sign-red: #e30613;
    --sign-yellow: #ffed00;
    --ink: #0b0b0b;
    --paper: #ffffff;
    --camera-tone: #8a8a8a;
  }
  html, body {
    margin: 0;
    padding: 0;
    width: 1200px;
    height: 943px;
    overflow: hidden;
    background: var(--paper);
  }
  .sign {
    position: relative;
    width: 1200px;
    height: 943px;
    font-family: "Jost", "Century Gothic", sans-serif;
  }
  .sign-frame {
    position: absolute;
    left: 27px;
    top: 29px;
    width: 1146px;
    height: 885px;
    box-sizing: border-box;
    border: 5px solid var(--ink);
    border-radius: 22px;
    background: var(--sign-red);
    overflow: hidden;
  }
  .title-banner {
    position: absolute;
    left: 42px;
    top: 21px;
    width: 1041px;
    height: 136px;
    box-sizing: border-box;
    border: 5px solid var(--ink);
    border-radius: 14px;
    background: var(--sign-yellow);
    display: flex;
    align-items: center;
    justify-content: center;
  }
  .title-banner h1 {
    margin: 0;
    font-size: 108px;
    font-weight: 700;
    letter-spacing: 2px;
    color: var(--ink);
    line-height: 1;
  }
  .info-panel {
    position: absolute;
    left: 7px;
    top: 189px;
    width: 1122px;
    height: 428px;
    background: var(--paper);
  }
  .camera-art {
    position: absolute;
    left: 42px;
    top: 44px;
    width: 524px;
    height: 328px;
    background: radial-gradient(ellipse at 60% 50%, #c4c4c4 0%, var(--camera-tone) 70%, #cfcfcf 100%);
    border-radius: 8px;
  }
  .site-address {
    position: absolute;
    left: 158px;
    top: 378px;
    margin: 0;
    font-size: 21px;
    font-weight: 700;
    color: var(--ink);
  }
  .protection-notice {
    position: absolute;
    left: 600px;
    top: 62px;
    width: 500px;
    margin: 0;
    text-align: center;
    font-size: 60px;
    font-weight: 700;
    line-height: 71px;
    color: var(--ink);
  }
  .recording-notice {
    position: absolute;
    left: 0;
    top: 650px;
    width: 1136px;
    margin: 0;
    text-align: center;
    font-size: 39px;
    font-weight: 700;
    line-height: 50.5px;
    letter-spacing: 0.5px;
    color: var(--paper);
  }
</style>
</head>
<body>
  <main class="sign">
    <div class="sign-frame">
      <header class="title-banner">
        <h1>SURVEILLANCE</h1>
      </header>
      <section class="info-panel">
        <div class="camera-art" role="img" aria-label="Black and white line drawing of a wall-mounted CCTV bullet camera with infrared LEDs around the lens"></div>
        <p class="site-address">www.varnotek.com</p>
        <p class="protection-notice">THIS PROPERTY<br>PROTECTED BY<br>CCTV SECURITY<br>CAMERAS</p>
      </section>
      <p class="recording-notice">FOR YOUR PERSONAL PROTECTION ALL ACTIVITIES<br>ARE RECORDED ON DIGITAL MEDIA<br>TO AID IN THE PROSECUTION OF ANY CRIME<br>COMMITTED ON THIS PROPERTY</p>
    </div>
  </main>
</body>
</html>
```